Webdesign für ORVI Registrierung für die USA
Zielgruppe
Erstellung von Reisegenehmigungen (Visa)
Aufgabenstellung
- Orientierung an Orvi.us
- es gibt kein Logo oder CD
- die Webseite soll seriös wirken

```html
<!DOCTYPE html>
<html lang="en">
<head>
<meta charset="utf-8">
<title>ORVI – United States Travel Authorization Application</title>
<link href="https://fonts.googleapis.com/css2?family=Playfair+Display:wght@700&family=Roboto:wght@400;500;700&display=swap" rel="stylesheet">
<style>
:root{
  --navy:#141a52;
  --red:#c8102e;
  --link:#2a3df0;
  --text:#4a4a55;
  --page:#ececec;
  --white:#ffffff;
}
*{box-sizing:border-box;margin:0;padding:0}
html,body{width:1200px;height:1181px;overflow:hidden}
body{background:var(--page);font-family:"Roboto",sans-serif;color:var(--text);position:relative}
.hero-backdrop{position:absolute;left:0;top:0;width:1200px;height:560px;
  background:
    linear-gradient(180deg,rgba(236,236,236,0) 55%,var(--page) 100%),
    linear-gradient(115deg,#1f2f86 0%,#2a3b94 30%,#d8d8e0 42%,#c8283a 55%,#f2f2f2 63%,#c42234 72%,#eeeeee 82%,#c9283a 100%);}
.site{position:absolute;left:232px;top:162px;width:736px}
.nav{height:26px;background:var(--navy);display:flex;align-items:center;padding:0 11px;gap:25px}
.nav a{color:var(--white);font-size:9.5px;font-weight:700;text-decoration:none;letter-spacing:.1px}
.nav .lang{margin-left:auto;font-weight:400;display:flex;align-items:center;gap:4px}
.masthead{background:var(--white);height:88px;display:flex;align-items:center;justify-content:space-between;padding:0 19px 0 11px}
.masthead h1{font-family:"Playfair Display",serif;font-size:34px;line-height:38px;color:var(--navy)}
.btn-apply{display:inline-flex;align-items:center;gap:10px;border:2px solid var(--red);border-radius:20px;color:var(--red);font-weight:500;font-size:15px;padding:0 21px;height:37px;text-decoration:none}
.tiles{display:flex;gap:19px;margin-top:19px}
.tile{width:170px;height:150px;background:var(--white);display:flex;flex-direction:column;align-items:center;justify-content:flex-end;padding-bottom:23px}
.tile-art{width:94px;height:68px;margin-bottom:16px;border-radius:4px}
.tile span{color:var(--navy);font-weight:500;font-size:14.5px}
.card{position:absolute;background:var(--white);padding:13px 12px 0 12px}
.card h2{font-family:"Playfair Display",serif;font-size:33px;line-height:38px;color:var(--navy);margin-bottom:12px}
.card p{font-size:12px;line-height:18.8px;hyphens:auto;-webkit-hyphens:auto}
.card p a{color:var(--link);font-weight:500}
.citizenship{position:absolute;left:735px;top:465px;width:232px;height:125px;background:var(--navy);padding:12px}
.citizenship label{color:var(--white);font-weight:500;font-size:12.5px;display:block;margin-bottom:9px}
.select{background:var(--white);height:32px;display:flex;align-items:center;justify-content:space-between;padding:0 9px;font-size:12px;color:#555}
.submit{position:absolute;right:13px;top:81px;width:94px;height:25px;border-radius:13px;background:var(--red);color:var(--white);font-weight:700;font-size:12.5px;display:flex;align-items:center;justify-content:center}
.eligibility h2{margin-bottom:10px}
.eligibility .btn-apply{margin:10px 0 12px 29px;height:37px;width:150px;justify-content:center;padding:0;color:var(--red)}
.footer{position:absolute;left:232px;top:1093px;width:736px;text-align:center}
.footer-nav{font-size:9.8px;font-weight:700;color:var(--navy);padding-bottom:6px;border-bottom:1px solid #333}
.footer-nav a{color:var(--navy);text-decoration:none}
.footer-nav i{font-style:normal;font-weight:400;margin:0 4px}
.footer small{display:block;font-size:9.5px;color:var(--navy);margin-top:11px}
.footer small+small{margin-top:6px}
</style>
</head>
<body>
<div class="hero-backdrop" role="img" aria-label="Waving American flag photograph"></div>

<div class="site">
  <nav class="nav">
    <a href="#">ORVI APPLICATION</a>
    <a href="#">VERIFY - LOCATE - CHECK ORVI STATUS</a>
    <a href="#">ORVI NUMBER</a>
    <a href="#">HELP</a>
    <a href="#" class="lang">English
      <svg width="8" height="5" viewBox="0 0 8 5"><path d="M1 1l3 3 3-3" fill="none" stroke="#fff" stroke-width="1.2"/></svg></a>
  </nav>
  <header class="masthead">
    <h1>United States<br>Travel Authorization Application</h1>
    <a href="#" class="btn-apply">APPLY NOW
      <svg width="12" height="11" viewBox="0 0 12 11"><path d="M1 1l4.5 4.5L1 10M6 1l4.5 4.5L6 10" fill="none" stroke="#c8102e" stroke-width="1.6"/></svg></a>
  </header>
  <div class="tiles">
    <div class="tile"><div class="tile-art" role="img" aria-label="Clipboard checklist illustration" style="background:linear-gradient(180deg,#e7dfe6,#d9c6cf)"></div><span>APPLY ONLINE</span></div>
    <div class="tile"><div class="tile-art" role="img" aria-label="Map of the U.S. in flag colours" style="background:linear-gradient(180deg,#c9cbe0,#e3c3c8)"></div><span>TRAVEL TO THE U.S.</span></div>
    <div class="tile"><div class="tile-art" role="img" aria-label="Group of business people illustration" style="background:linear-gradient(180deg,#d0d2e6,#c5c8df)"></div><span>IMMIGRATION</span></div>
    <div class="tile"><div class="tile-art" role="img" aria-label="Handshake illustration" style="background:linear-gradient(135deg,#c9cbe0,#e5c2c7)"></div><span>WELCOME</span></div>
  </div>
</div>

<section class="card" style="left:232px;top:465px;width:484px;height:176px">
  <h2>What is ORVI?</h2>
  <p>ORVI stands for Online Registration for Visitor Identification. ORVI is an <a href="#">online application system</a> developed by the United States government to pre-screen travelers before they are allow to board an airplane or ship bound for the United States. Starting on January 12, 2009, any person entering the United States under the visa waiver program is required to hold an approved ORVI Travel Authorization.</p>
</section>

<section class="card" style="left:232px;top:659px;width:484px;height:177px">
  <h2>Who Needs to Apply for ORVI?</h2>
  <p>All travelers entering the United States (by air or sea) under the visa waiver program are required to hold a valid ORVI travel authorization. The purpose of <a href="#">ORVI</a> is to allow DHS to pre-screen all Visa Waiver Travelers before they leave their respective countries. U.S.-bound travelers are recommended to apply for a Travel Authorization at least 72 hours prior to departure.</p>
</section>

<section class="card" style="left:232px;top:853px;width:484px;height:214px">
  <h2>What is the Visa Waiver<br>Program?</h2>
  <p>The visa waiver program is a U.S. government program that enables citizens and nationals from the <a href="#">Visa Waiver Countries</a> to enter the United States for tourism or business purposes for up to 90 days without obtaining a visa. The advantage of entering the United States under the visa waiver program is that you can travel to the United States on short notice without obtaining a visa.</p>
</section>

<form class="citizenship">
  <label>Select your Citizenship:</label>
  <div class="select">--- Select ---
    <svg width="10" height="6" viewBox="0 0 10 6"><path d="M1 1l4 4 4-4" fill="none" stroke="#333" stroke-width="1.3"/></svg></div>
  <div class="submit">submit</div>
</form>

<section class="card eligibility" style="left:735px;top:609px;width:232px;height:458px">
  <h2>Free ORVI<br>Eliggibility<br>Test</h2>
  <p>Only citizens of <a href="#">Visa Waiver Countries</a> are allowed to apply for ORVI. It is important to know if you qualify for ORVI before you submit your application. Use the drop-down menu on the left to select your nationality and click on "Submit".</p>
  <a href="#" class="btn-apply">APPLY NOW
    <svg width="12" height="11" viewBox="0 0 12 11"><path d="M1 1l4.5 4.5L1 10M6 1l4.5 4.5L6 10" fill="none" stroke="#c8102e" stroke-width="1.6"/></svg></a>
  <p>The ORVI application system is entirely online. There are no forms that need to be printed and you do not have to go to a U.S. Embassy or Consulate in person. Download the <a href="#">ORVI Application</a> Guide and apply today!</p>
</section>

<footer class="footer">
  <div class="footer-nav"><a href="#">HOME</a><i>|</i><a href="#">APPLICATION</a><i>|</i><a href="#">FAQ</a><i>|</i><a href="#">PRIVACY POLICY</a><i>|</i><a href="#">TERMS and CONDITIONS</a><i>|</i><a href="#">CONTACT US</a></div>
  <small>Legal Disclaimer: ORVI.US is a private information website not affiliated with the United States Government.</small>
  <small>© 2017 ORVI APPLICATION SERVICES (www.orvi.us) - All Rights Reserved</small>
</footer>
</body>
</html>
```